Willow Table Kitchen February contest

The website slider is 990 X 225 pixels to fit in with this website www.willowtablekitchen.com.au
We would love a fun, lively, food-oriented slider created for Willow Table Kitchen website. Willow Table Kitchen is a central place where people who love food, cooking for their family and friends, and sharing recipes can hang out. We'd like the sliders to be simple, bright and to entice people to click on the link.
The banner ad needs to feature the Kestral mixer, and to use a colour scheme that also works with the existing website. There's a blog with more information on the Kestral mixer here http://willowtablekitchen.com.au/uncategorized/upload-a-recipe-in-february-to-be-in-the-running-to-win-a-kestral-mixer/
A slider in December was used to promote a similar competition which I will upload as inspiration, along with the image of the Kestral mixer to use.
Main text: Add your best recipe by February 28 to win!
Smaller text: Best recipe as chosen by Willow Table Kitchen editors will win a Kestral mixer worth $699.
Target Market(s)
Food lovers - home cooks and food bloggers. Mainly women, 30+
Industry/Entity Type
Chef
Look and feel
Each slider illustrates characteristics of the customer's brand and the style your logo design should communicate.

```html
<!DOCTYPE html>
<html lang="en">
<head>
<meta charset="utf-8">
<title>Willow Table Kitchen</title>
<link rel="stylesheet" href="https://fonts.googleapis.com/css2?family=Arimo:wght@400;700&family=Dancing+Script:wght@500&family=Rokkitt:wght@300;400&display=swap">
<style>
  :root {
    --paper: #efe5d8;
    --white: #ffffff;
    --ink: #3a3330;
    --brown: #4a3a33;
    --accent: #d9522b;
    --link: #cc4a35;
    --sky: #2ba7d2;
    --sky-deep: #1f93bd;
    --gold: #f5dd94;
    --card: #f8f0e8;
    --card-edge: #f2d39d;
    --star: #c95a5e;
    --star-off: #d8d2cc;
    --search: #fcf1e6;
    --muted: #6c6460;
  }
  * { box-sizing: border-box; margin: 0; padding: 0; }
  html, body { width: 1200px; height: 737px; overflow: hidden; }
  body {
    background: var(--paper);
    font-family: "Arimo", Arial, sans-serif;
    color: var(--ink);
  }
  .page {
    position: relative;
    width: 1170px;
    height: 719px;
    transform: scale(1.02564);
    transform-origin: 0 0;
  }
  .abs { position: absolute; }

  /* Header */
  .account {
    left: 962px; top: 0; width: 121px; height: 28px;
    background: var(--white); border-radius: 0 0 4px 4px;
    display: flex; align-items: center; justify-content: center; gap: 14px;
    font-size: 12px; color: var(--link);
  }
  .brand {
    left: 93px; top: -16px; width: 178px; height: 178px;
    border-radius: 50%; background: var(--white);
    display: flex; align-items: center; justify-content: center; text-align: center;
    font-family: "Arimo", Arial, sans-serif; font-weight: 700; font-size: 20px; line-height: 1.2;
    color: var(--brown); z-index: 3; padding: 24px 30px 0;
  }
  .join {
    left: 428px; top: 32px;
    font-family: "Dancing Script", cursive; font-weight: 500; font-size: 28px; color: var(--brown);
  }
  .join-arrow { left: 783px; top: 38px; }

  /* Navigation */
  .nav-main {
    left: 278px; top: 100px; width: 305px; height: 40px; background: var(--white);
    display: flex; align-items: center; gap: 20px; padding-left: 24px;
    font-size: 12px; color: var(--ink);
  }
  .nav-main span { display: flex; align-items: center; gap: 5px; }
  .nav-bar {
    left: 583px; top: 100px; width: 500px; height: 40px; background: var(--accent);
    border-radius: 0 4px 0 0;
    display: flex; align-items: center; padding-left: 32px;
    font-size: 12px; font-weight: 700; color: var(--white);
  }
  .nav-bar span + span::before {
    content: ""; display: inline-block; width: 4px; height: 4px; border-radius: 50%;
    background: var(--white); margin: 0 11px 2px; vertical-align: middle;
  }

  /* Slider */
  .slider { left: 93px; top: 144px; width: 990px; height: 225px; background: var(--white); }
  .photo-cheese { left: 93px; top: 144px; width: 188px; height: 225px;
    background: radial-gradient(ellipse at 55% 45%, #f6ecc6 0%, #e9dba6 45%, #7fb6cf 90%); }
  .promo {
    left: 283px; top: 144px; width: 312px; height: 225px;
    background: repeating-linear-gradient(90deg, var(--sky) 0 3px, var(--sky-deep) 3px 4px);
    color: var(--white); text-align: center; font-family: "Rokkitt", serif;
  }
  .promo-kicker { margin-top: 30px; font-size: 20px; font-weight: 400; display: flex; align-items: center; justify-content: center; gap: 10px; }
  .promo-kicker::before, .promo-kicker::after { content: ""; width: 26px; height: 1px; background: var(--white); }
  .promo-date { font-size: 27px; font-weight: 400; letter-spacing: 1px; margin-top: 2px; }
  .promo-win { font-size: 60px; font-weight: 400; color: var(--gold); line-height: 1; margin-top: 4px; letter-spacing: 1px; }
  .promo-small { font-family: "Arimo", sans-serif; font-weight: 700; font-size: 14px; color: var(--gold); line-height: 18px; margin-top: 10px; padding: 0 18px; }
  .photo-mixer { left: 600px; top: 156px; width: 252px; height: 206px;
    background: radial-gradient(ellipse at 50% 55%, #d7dadc 0%, #bfe6f2 38%, #ffffff 72%); }
  .photo-rice { left: 862px; top: 144px; width: 221px; height: 225px;
    background: radial-gradient(ellipse at 50% 55%, #c9772f 0%, #b3602a 45%, #7fb9c7 95%); }

  .content { left: 93px; top: 369px; width: 990px; height: 350px; background: var(--white); }

  /* Section headings */
  .heading { display: flex; align-items: center; gap: 10px; font-size: 20px; font-weight: 400; color: var(--ink); }

  /* Recipe cards */
  .card { top: 438px; width: 200px; height: 276px; background: var(--card); border-bottom: 5px solid var(--card-edge); }
  .card-photo { height: 135px; }
  .card-title { font-size: 14px; margin: 14px 0 0 10px; white-space: nowrap; }
  .card-author { font-size: 12px; color: var(--link); margin: 10px 0 0 10px; }
  .card-meta { position: absolute; left: 10px; right: 10px; bottom: 12px; display: flex; justify-content: space-between; align-items: center; font-size: 12px; }
  .card-meta .count { display: flex; align-items: center; gap: 3px; }

  .rating { position: relative; display: inline-block; font-size: 18px; line-height: 1; letter-spacing: -1px; color: var(--star-off); }
  .rating .fill { position: absolute; left: 0; top: 0; overflow: hidden; white-space: nowrap; color: var(--star); }

  /* Sidebar */
  .search { left: 773px; top: 384px; width: 297px; height: 38px; background: var(--search); border: 1px solid #efdccb; border-radius: 3px;
    display: flex; align-items: center; justify-content: space-between; padding: 0 12px; font-size: 14px; font-style: italic; color: var(--muted); }
  .search-scope { left: 937px; top: 428px; font-size: 12px; color: var(--muted); display: flex; gap: 16px; }
  .search-scope span { display: flex; align-items: center; gap: 5px; }
  .radio { width: 11px; height: 11px; border-radius: 50%; border: 1px solid #999; background: #eee; display: inline-flex; align-items: center; justify-content: center; }
  .radio.on::after { content: ""; width: 5px; height: 5px; border-radius: 50%; background: #666; }

  .top-item { left: 773px; width: 300px; height: 90px; }
  .top-photo { position: absolute; left: 0; top: 0; width: 134px; height: 90px; }
  .top-rank { position: absolute; left: -14px; top: 26px; width: 34px; height: 34px; border-radius: 50%; background: var(--white);
    display: flex; align-items: center; justify-content: center; font-size: 12px; color: #d9a67a; padding-left: 10px; }
  .top-title { position: absolute; left: 144px; top: 0; font-size: 12.5px; line-height: 20px; width: 154px; }
  .top-author { position: absolute; left: 144px; font-size: 12.5px; color: var(--link); }
  .top-item .rating { position: absolute; left: 144px; top: 75px; }
</style>
</head>
<body>
<div class="page">

  <div class="abs account"><span>Register</span><span>Login</span></div>
  <div class="abs brand">Willow Table Kitchen</div>
  <div class="abs join">Join the community now!</div>
  <svg class="abs join-arrow" width="46" height="26" viewBox="0 0 46 26" aria-hidden="true">
    <path d="M2 22 Q24 24 42 4" fill="none" stroke="var(--accent)" stroke-width="2" stroke-linecap="round"/>
    <path d="M34 5 L43 3 L42 12" fill="none" stroke="var(--accent)" stroke-width="2" stroke-linecap="round"/>
  </svg>

  <nav class="abs nav-main">
    <span><svg width="20" height="14" viewBox="0 0 20 14" aria-hidden="true"><path d="M1 5 H19 Q18 13 10 13 Q2 13 1 5Z" fill="var(--accent)"/><path d="M11 5 L17 0" stroke="var(--accent)" stroke-width="2"/></svg>Recipes</span>
    <span><svg width="18" height="16" viewBox="0 0 18 16" aria-hidden="true"><circle cx="5" cy="6" r="4" fill="var(--accent)"/><circle cx="13" cy="6" r="4" fill="var(--accent)"/><circle cx="9" cy="4" r="4" fill="var(--accent)"/><rect x="4" y="8" width="10" height="7" rx="1" fill="var(--accent)"/></svg>Chefs</span>
    <span><svg width="20" height="16" viewBox="0 0 20 16" aria-hidden="true"><circle cx="5" cy="4" r="3" fill="var(--accent)"/><circle cx="15" cy="4" r="3" fill="var(--accent)"/><circle cx="10" cy="7" r="3" fill="var(--accent)"/><ellipse cx="5" cy="11" rx="4" ry="3" fill="var(--accent)"/><ellipse cx="15" cy="11" rx="4" ry="3" fill="var(--accent)"/><ellipse cx="10" cy="14" rx="4" ry="2.5" fill="var(--accent)"/></svg>Mentors</span>
  </nav>
  <nav class="abs nav-bar">
    <span>Upload your recipe</span><span>Prizes</span><span>About</span><span>FAQs</span><span>Contact</span><span>Blog</span>
  </nav>

  <div class="abs slider"></div>
  <div class="abs photo-cheese" role="img" aria-label="Bowl of freshly grated cheese"></div>
  <div class="abs promo">
    <div class="promo-kicker">Add your best recipe</div>
    <div class="promo-date">BY FEBRUARY 28</div>
    <div class="promo-win">TO WIN!</div>
    <div class="promo-small">Best recipe as chosen by Willow Table Kitchen editors will win a</div>
  </div>
  <div class="abs photo-mixer" role="img" aria-label="Kestral stand mixer in white and sky blue with a steel bowl"></div>
  <div class="abs photo-rice" role="img" aria-label="Mound of spiced tomato rice on a blue plate"></div>

  <div class="abs content"></div>

  <h2 class="abs heading" style="left:105px; top:394px;">
    <svg width="22" height="16" viewBox="0 0 22 16" aria-hidden="true"><path d="M1 6 H21 Q20 15 11 15 Q2 15 1 6Z" fill="var(--accent)"/><path d="M12 6 L19 0" stroke="var(--accent)" stroke-width="2"/></svg>
    <span>Featured Recipes</span>
  </h2>

  <article class="abs card" style="left:103px;">
    <div class="card-photo" role="img" aria-label="Open cacciatore lasagne on a white plate" style="background:radial-gradient(ellipse at 50% 50%, #d9a46a 0%, #b4552e 40%, #e8e4df 80%);"></div>
    <div class="card-title">Open Cacciatore Lasagne</div>
    <div class="card-author">By Carla Denholm</div>
    <div class="card-meta">
      <span class="rating">★★★★★<span class="fill" style="width:88%;">★★★★★</span></span>
      <span class="count"><svg width="22" height="16" viewBox="0 0 22 16" aria-hidden="true"><circle cx="11" cy="8" r="7" fill="var(--accent)"/><circle cx="11" cy="8" r="4" fill="none" stroke="var(--white)" stroke-width="1"/><rect x="1" y="2" width="1.5" height="12" fill="var(--accent)"/><rect x="19.5" y="2" width="1.5" height="12" fill="var(--accent)"/></svg>10</span>
    </div>
  </article>

  <article class="abs card" style="left:323px;">
    <div class="card-photo" role="img" aria-label="Spaghetti bolognese topped with grated cheese" style="background:radial-gradient(ellipse at 50% 45%, #7a3a22 0%, #d6b17a 45%, #8a4a3c 90%);"></div>
    <div class="card-title">Spaghetti Bologanise</div>
    <div class="card-author">By Lucy Sanderson</div>
    <div class="card-meta">
      <span class="rating">★★★★★<span class="fill" style="width:88%;">★★★★★</span></span>
      <span class="count"><svg width="22" height="16" viewBox="0 0 22 16" aria-hidden="true"><circle cx="11" cy="8" r="7" fill="var(--accent)"/><circle cx="11" cy="8" r="4" fill="none" stroke="var(--white)" stroke-width="1"/><rect x="1" y="2" width="1.5" height="12" fill="var(--accent)"/><rect x="19.5" y="2" width="1.5" height="12" fill="var(--accent)"/></svg>3</span>
    </div>
  </article>

  <article class="abs card" style="left:543px;">
    <div class="card-photo" role="img" aria-label="Bowl of clear vegetable stock with potato and greens" style="background:radial-gradient(ellipse at 45% 55%, #9b8a3a 0%, #6d7a36 40%, #dcdcd8 85%);"></div>
    <div class="card-title">Clean Eating Vegetable Stock</div>
    <div class="card-author">By Janet Holloway</div>
    <div class="card-meta">
      <span class="rating">★★★★★<span class="fill" style="width:100%;">★★★★★</span></span>
      <span class="count"><svg width="22" height="16" viewBox="0 0 22 16" aria-hidden="true"><circle cx="11" cy="8" r="7" fill="var(--accent)"/><circle cx="11" cy="8" r="4" fill="none" stroke="var(--white)" stroke-width="1"/><rect x="1" y="2" width="1.5" height="12" fill="var(--accent)"/><rect x="19.5" y="2" width="1.5" height="12" fill="var(--accent)"/></svg>3</span>
    </div>
  </article>

  <div class="abs search">
    <span>search</span>
    <svg width="24" height="24" viewBox="0 0 24 24" aria-hidden="true"><circle cx="10" cy="10" r="7" fill="none" stroke="#f0b87a" stroke-width="2.5"/><path d="M15 15 L22 22" stroke="#f0b87a" stroke-width="3" stroke-linecap="round"/></svg>
  </div>
  <div class="abs search-scope">
    <span>Recipes <i class="radio on"></i></span>
    <span>Chefs <i class="radio"></i></span>
  </div>

  <h2 class="abs heading" style="left:775px; top:463px;">
    <svg width="22" height="16" viewBox="0 0 22 16" aria-hidden="true"><path d="M1 6 H21 Q20 15 11 15 Q2 15 1 6Z" fill="var(--accent)"/><path d="M12 6 L19 0" stroke="var(--accent)" stroke-width="2"/></svg>
    <span>Highest Rated Recipes</span>
  </h2>

  <div class="abs top-item" style="top:507px;">
    <div class="top-photo" role="img" aria-label="White chocolate parfait with strawberry and mint" style="background:radial-gradient(ellipse at 50% 50%, #f3e3c4 0%, #e2b46a 45%, #d8d4cf 90%);"></div>
    <div class="top-rank">1</div>
    <div class="top-title">White Chocolate Parfait W/&nbsp;Lemon Curd and Short ...</div>
    <div class="top-author" style="top:62px;">By Simon Tarrant</div>
    <span class="rating">★★★★★<span class="fill" style="width:100%;">★★★★★</span></span>
  </div>

  <div class="abs top-item" style="top:617px;">
    <div class="top-photo" role="img" aria-label="Tray of glazed hot cross buns" style="background:radial-gradient(ellipse at 50% 55%, #b06a35 0%, #7a4326 50%, #3b2a22 95%);"></div>
    <div class="top-rank">2</div>
    <div class="top-title">Hot Cross Buns</div>
    <div class="top-author" style="top:22px;">By Mira Gorski</div>
    <span class="rating">★★★★★<span class="fill" style="width:100%;">★★★★★</span></span>
  </div>

</div>
</body>
</html>
```